Harbor Vantage Web Design Project

We need a website design for a start up company called "Harbor Vantage". We provide business consultancy services as well as technology-related services (IT). The design should communicate simplicity and elegance. The domain name of the site will be harborvantage-example.com. The logo of the company is https://files.example-share.net/u/7418205/4630_2116587_67315_image.jpg

Target Market(s)

SMB, Corporates, Semi-governments, Governments.

Industry/Entity Type

Business

Requirements
Must have
• - The background of the pages should be white or soft grey, but we are open for suggestions.
- The pages should have nice menu animations.
- The pages should be "portal-style", with multiple placeholders for different sections and multiple tabs.
Nice to have
• The page should auto-fit the screen and scroll vertically as much as needed.
Should not have
• - Flash Animations.
- Generic Photos.

```html
<!DOCTYPE html>
<html lang="en">
<head>
<meta charset="utf-8">
<title>Harbor Vantage</title>
<link href="https://fonts.googleapis.com/css2?family=Open+Sans:wght@400;600;700;800&family=Questrial&display=swap" rel="stylesheet">
<style>
:root{
  --white:#ffffff;
  --page:#e4e2dd;
  --dark:#2d2d2d;
  --darker:#1f1f1f;
  --blue:#2a82b5;
  --cyan:#1aa3d9;
  --heading-blue:#1d7fa8;
  --red:#c0161f;
  --red-dark:#9c1018;
  --text:#333333;
  --green:#4f9a1a;
  --dash:#7fb6d6;
}
*{margin:0;padding:0;box-sizing:border-box}
html,body{width:845px;height:1200px;overflow:hidden}
body{position:relative;background:var(--page);font-family:"Open Sans",sans-serif;color:var(--text)}
.abs{position:absolute}

.site-header{left:0;top:0;width:845px;height:139px;background:var(--white)}
.brand{left:96px;top:48px;display:flex;align-items:center;gap:10px}
.brand-mark{width:22px;height:22px;border-radius:50%;background:var(--blue)}
.brand-name{font-size:25px;font-weight:700;color:var(--blue);letter-spacing:-.3px}
.call-tab{left:601px;top:0;width:156px;height:110px}
.call-text{left:601px;top:40px;width:156px;text-align:center;color:var(--white)}
.call-text .big{font-size:21px;font-weight:800;line-height:1.1}
.call-text .small{font-size:14px;font-weight:700}

.band{left:0;top:139px;width:845px;height:198px;background:var(--dark)}
.main-nav{left:0;top:150px;height:26px;width:845px}
.main-nav a{position:absolute;top:3px;color:var(--white);font-size:13px;text-decoration:none}
.main-nav a.active{font-weight:700}
.nav-marker{left:106px;top:139px;width:44px;height:5px;background:var(--cyan)}
.btn{top:152px;height:20px;border-radius:3px;color:var(--white);font-size:13px;font-weight:700;text-align:center;line-height:20px}
.btn-login{left:634px;width:53px;background:var(--blue)}
.btn-signup{left:696px;width:61px;background:var(--red)}

.hero{left:96px;top:181px;width:662px;height:265px;background:linear-gradient(120deg,#6f7377 0%,#c9cbcd 30%,#2fa0dc 45%,#c3c5c7 65%,#8f9194 100%);box-shadow:0 3px 6px rgba(0,0,0,.35)}
.hero-caption{left:473px;top:285px;width:285px;height:91px;background:rgba(40,45,52,.75);border-radius:10px 0 0 10px}
.hero-caption p{position:absolute;left:24px;top:10px;color:var(--white);font-size:15px;font-weight:700;line-height:19px}
.hero-more{position:absolute;right:30px;top:54px;background:#2c7fa9;color:var(--white);font-size:12px;font-weight:700;padding:1px 6px;border-radius:3px}

.sidebar{left:95px;top:482px;width:176px;height:336px;background:var(--white);border-radius:0 0 8px 8px}
.panel-head{height:22px;color:var(--white);font-size:15px;font-weight:700;line-height:22px;padding-left:14px}
.sidebar .panel-head{background:var(--blue)}
.hot-links{list-style:none}
.hot-links li{position:relative;height:29.6px;border-bottom:1.5px dashed var(--dash);font-size:13px;line-height:29px;padding-left:14px}
.hot-links li.active{color:var(--blue);font-weight:700}
.hot-links svg{position:absolute;right:9px;top:7px}
.sidebar-visual{left:101px;top:694px;width:163px;height:116px;background:radial-gradient(circle at 60% 40%,#6f9fc4,#1e3f5e 85%)}
.search-box{left:95px;top:828px;width:176px;height:44px;background:var(--white)}
.search-label{position:absolute;left:13px;top:9px;font-size:12px;font-weight:800;color:#222}
.search-field{position:absolute;left:66px;top:10px;width:78px;height:14px;background:#5b5b5b;border-radius:3px;color:#eee;font-size:9px;line-height:14px;padding-left:13px}
.search-icon{position:absolute;left:148px;top:9px}
.search-sub{position:absolute;left:13px;top:27px;font-size:8px;color:#444}

.content{left:283px;top:482px;width:474px;height:390px;background:var(--white);border-radius:0 0 6px 6px}
.content .panel-head{background:var(--dark)}
.content h2{position:absolute;font-family:"Questrial",sans-serif;color:var(--heading-blue);font-size:15px;font-weight:700}
.content p{position:absolute;font-size:11px;line-height:12.6px;color:#333}
.ticks{position:absolute;left:26px;top:233px;list-style:none;font-size:11px}
.ticks li{height:16.6px;display:flex;align-items:center;gap:7px}
.learn-btn{position:absolute;left:19px;top:330px;width:113px;height:22px;border:1px solid #c9c9c9;border-radius:3px;background:linear-gradient(#fafafa,#e2e2e2);font-size:8px;color:#2a6ea0;line-height:20px;padding-left:9px}
.learn-btn svg{position:absolute;right:6px;top:7px}

.product{width:121px;height:79px;background:var(--red);color:var(--white);box-shadow:1px 2px 3px rgba(0,0,0,.3)}
.product h3{position:absolute;left:4px;top:7px;font-size:12px;font-weight:700}
.product p{position:absolute;left:4px;top:29px;width:100px;font-size:8.5px;line-height:10.5px}
.product svg.go{position:absolute;right:6px;bottom:5px}
.fold{width:0;height:0;border-left:18px solid transparent;border-bottom:9px solid #111}

.footer{left:0;top:903px;width:845px;height:260px;background:var(--dark);border-top:6px solid #bdbbb6}
.footer h4{position:absolute;color:var(--cyan);font-family:"Questrial",sans-serif;font-weight:700;font-size:14px}
.quote{position:absolute;left:111px;width:268px;color:var(--white);font-size:11px;line-height:12.7px}
.quote cite{display:block;text-align:right;color:var(--cyan);font-weight:700;font-style:italic;margin-top:4px}
.partner{width:95px;height:84px;background:linear-gradient(160deg,#f1f1f1,#9aa3ad 60%,#3c4048)}
.bottom-nav{left:0;top:1163px;width:845px;height:37px;background:var(--darker);display:flex;justify-content:center;align-items:center}
.bottom-nav a{color:var(--white);text-decoration:none;font-size:13px;padding:0 9px;border-left:1px solid #888;line-height:18px}
.bottom-nav a:first-child{border-left:none}
</style>
</head>
<body>

<header class="site-header abs">
  <div class="brand abs"><span class="brand-mark"></span><span class="brand-name">Harbor Vantage</span></div>
</header>
<svg class="call-tab abs" viewBox="0 0 156 110" aria-hidden="true"><path d="M0 0H156V96L78 110L0 96Z" fill="#c0161f"/></svg>
<div class="call-text abs"><div class="big">Call us now</div><div class="small">1800 - harbor</div></div>

<div class="band abs"></div>
<div class="nav-marker abs"></div>
<nav class="main-nav abs">
  <a class="active" style="left:110px" href="#">Home</a>
  <a style="left:164px" href="#">About Us</a>
  <a style="left:234px" href="#">Our Services</a>
  <a style="left:320px" href="#">Our products</a>
  <a style="left:414px" href="#">Be Involved</a>
  <a style="left:496px" href="#">Contact Us</a>
</nav>
<div class="btn btn-login abs">Login</div>
<div class="btn btn-signup abs">Sign Up</div>

<div class="hero abs" role="img" aria-label="Close-up of a keyboard with a blue cloud key"></div>
<div class="hero-caption abs">
  <p>Store your company files in our<br>cloud now safer than ever.</p>
  <span class="hero-more">Learn More</span>
</div>

<aside class="sidebar abs">
  <div class="panel-head">Hot Links</div>
  <ul class="hot-links">
    <li class="active">Home<svg width="16" height="16" viewBox="0 0 16 16"><circle cx="8" cy="8" r="8" fill="#2a82b5"/><path d="M6 4l4 4-4 4" stroke="#fff" stroke-width="2" fill="none"/></svg></li>
    <li>About Us<svg width="16" height="16" viewBox="0 0 16 16"><circle cx="8" cy="8" r="8" fill="#2a82b5"/><path d="M6 4l4 4-4 4" stroke="#fff" stroke-width="2" fill="none"/></svg></li>
    <li>Our Services<svg width="16" height="16" viewBox="0 0 16 16"><circle cx="8" cy="8" r="8" fill="#2a82b5"/><path d="M6 4l4 4-4 4" stroke="#fff" stroke-width="2" fill="none"/></svg></li>
    <li>Our products<svg width="16" height="16" viewBox="0 0 16 16"><circle cx="8" cy="8" r="8" fill="#2a82b5"/><path d="M6 4l4 4-4 4" stroke="#fff" stroke-width="2" fill="none"/></svg></li>
    <li>Be Involved<svg width="16" height="16" viewBox="0 0 16 16"><circle cx="8" cy="8" r="8" fill="#2a82b5"/><path d="M6 4l4 4-4 4" stroke="#fff" stroke-width="2" fill="none"/></svg></li>
    <li>Contact Us<svg width="16" height="16" viewBox="0 0 16 16"><circle cx="8" cy="8" r="8" fill="#2a82b5"/><path d="M6 4l4 4-4 4" stroke="#fff" stroke-width="2" fill="none"/></svg></li>
  </ul>
</aside>
<div class="sidebar-visual abs" role="img" aria-label="Open hand holding a glowing cloud on a blue background"></div>
<div class="search-box abs">
  <span class="search-label">SEARCH</span>
  <span class="search-field">Search site</span>
  <svg class="search-icon" width="16" height="16" viewBox="0 0 16 16"><circle cx="6" cy="6" r="4.5" stroke="#333" stroke-width="1.8" fill="none"/><path d="M9.5 9.5L15 15" stroke="#333" stroke-width="2.2"/></svg>
  <span class="search-sub">Advanced Search | Tips</span>
</div>

<main class="content abs">
  <div class="panel-head">About Us</div>
  <h2 style="left:14px;top:30px">Why to choose harbor vantage</h2>
  <p style="left:14px;top:60px;width:326px">Lorem Ipsum is simply dummy text of the printing and typesetting industry. Lorem Ipsum has been the industry's standard dummy text ever since the 1500s, when an unknown printer took a galley of type and scrambled it to make a type specimen book. It has survived not only five centuries, but also the leap into electronic typesetting, remaining essentially unchanged. It was popularised in the 1960s.</p>
  <h2 style="left:15px;top:162px">Make you life easier with quickledger</h2>
  <p style="left:17px;top:191px;width:310px">Lorem Ipsum is simply dummy text of the printing and typesetting industry. Lorem Ipsum has been the industry's standard dummy text ever since the 1500s.</p>
  <ul class="ticks">
    <li><svg width="14" height="11" viewBox="0 0 14 11"><path d="M1 5.5l4 4L13 1" stroke="#4f9a1a" stroke-width="2.6" fill="none"/></svg>When an unknown printer</li>
    <li><svg width="14" height="11" viewBox="0 0 14 11"><path d="M1 5.5l4 4L13 1" stroke="#4f9a1a" stroke-width="2.6" fill="none"/></svg>Took a galley of type and scrambled</li>
    <li><svg width="14" height="11" viewBox="0 0 14 11"><path d="M1 5.5l4 4L13 1" stroke="#4f9a1a" stroke-width="2.6" fill="none"/></svg>Lorem Ipsum is simply dummy text</li>
    <li><svg width="14" height="11" viewBox="0 0 14 11"><path d="M1 5.5l4 4L13 1" stroke="#4f9a1a" stroke-width="2.6" fill="none"/></svg>Of the printing and typesetting</li>
    <li><svg width="14" height="11" viewBox="0 0 14 11"><path d="M1 5.5l4 4L13 1" stroke="#4f9a1a" stroke-width="2.6" fill="none"/></svg>Dummy text ever since the 1500s</li>
  </ul>
  <div class="learn-btn">Learn More<svg width="14" height="6" viewBox="0 0 14 6"><path d="M0 3H13M10 0l3 3-3 3" stroke="#2a6ea0" fill="none"/></svg></div>
</main>

<div class="fold abs" style="left:757px;top:545px"></div>
<div class="product abs" style="left:654px;top:554px"><h3>Product 1</h3><p>Lorem Ipsum is simply dummy text of the printing</p><svg class="go" width="15" height="15" viewBox="0 0 16 16"><circle cx="8" cy="8" r="8" fill="#222"/><path d="M6 4l4 4-4 4" stroke="#fff" stroke-width="2" fill="none"/></svg></div>
<div class="fold abs" style="left:757px;top:647px"></div>
<div class="product abs" style="left:654px;top:656px"><h3>Product 2</h3><p>Lorem Ipsum is simply dummy text of the printing</p><svg class="go" width="15" height="15" viewBox="0 0 16 16"><circle cx="8" cy="8" r="8" fill="#222"/><path d="M6 4l4 4-4 4" stroke="#fff" stroke-width="2" fill="none"/></svg></div>
<div class="fold abs" style="left:757px;top:751px"></div>
<div class="product abs" style="left:654px;top:760px"><h3>Product 3</h3><p>Lorem Ipsum is simply dummy text of the printing</p><svg class="go" width="15" height="15" viewBox="0 0 16 16"><circle cx="8" cy="8" r="8" fill="#222"/><path d="M6 4l4 4-4 4" stroke="#fff" stroke-width="2" fill="none"/></svg></div>

<footer class="footer abs">
  <h4 style="left:112px;top:18px">Testimonials</h4>
  <h4 style="left:448px;top:18px">Partners</h4>
  <div class="quote" style="top:53px">Lorem Ipsum is simply dummy text of the printing and typesetting industry. Lorem Ipsum has been the industry's standard dummy text ever since the 1500s.<cite>Delia R.</cite></div>
  <div class="quote" style="top:138px">Lorem Ipsum is simply dummy text of the printing and typesetting industry. Lorem Ipsum has been the industry's standard dummy text ever since the 1500s.<cite>Marcus T.</cite></div>
</footer>
<div class="partner abs" style="left:436px;top:960px" role="img" aria-label="Partner portrait: businessman on a phone call"></div>
<div class="partner abs" style="left:544px;top:960px" role="img" aria-label="Partner portrait: businessman on a phone call"></div>
<div class="partner abs" style="left:649px;top:960px" role="img" aria-label="Partner portrait: smiling businessman with team"></div>
<div class="partner abs" style="left:436px;top:1055px" role="img" aria-label="Partner portrait: business team giving thumbs up"></div>
<div class="partner abs" style="left:544px;top:1055px" role="img" aria-label="Partner portrait: business team giving thumbs up"></div>
<div class="partner abs" style="left:649px;top:1055px" role="img" aria-label="Partner portrait: support agent with headset"></div>

<nav class="bottom-nav abs">
  <a href="#">Home</a><a href="#">About Us</a><a href="#">Our Services</a><a href="#">Our products</a><a href="#">Be Involved</a><a href="#">Contact Us</a>
</nav>

</body>
</html>
```